Business Card Design Project

We need a Business Card for an Mechanical Engineering firm in Singapore. The design should be Modern & Technical looking, yet eye catching.

Our company deals in Cutting Tools & Machine Accessories for the Manufacturing Industries such as Oil & Gas, Aero Space, etc... For more information on our Company, you can either email me or view our website www.valtrion.com.sg.

We are trying to revamp our image to give our consumers a fresh new perspective to our company, so we welcome all ideas.

Industry/Entity Type

Business

Requirements
Must have
• Must incorporate New Company Logo into the card as shown in Uploaded file.

```html
<!DOCTYPE html>
<html lang="en">
<head>
<meta charset="utf-8">
<title>Valtrion Tools – Business Card</title>
<link href="https://fonts.googleapis.com/css2?family=Lato:wght@400;700&display=swap" rel="stylesheet">
<style>
  :root {
    --brand: #a0063a;
    --ink: #2b2b2b;
    --paper: #ffffff;
    --backdrop: #e6e9ec;
  }
  * { box-sizing: border-box; margin: 0; padding: 0; }
  html, body { width: 1200px; height: 960px; overflow: hidden; }
  body {
    background: var(--backdrop);
    font-family: "Lato", Arial, sans-serif;
    color: var(--ink);
    position: relative;
  }
  .card {
    position: absolute;
    left: 250px;
    width: 700px;
    height: 400px;
    box-shadow: 0 6px 20px rgba(0,0,0,0.18);
    overflow: hidden;
  }
  .card--front { top: 60px; background: var(--paper); }
  .card--back  { top: 500px; background: var(--brand); }

  .wordmark {
    display: flex;
    align-items: center;
    gap: 10px;
    font-weight: 700;
    letter-spacing: 1px;
    text-transform: uppercase;
  }
  .wordmark__dot {
    border-radius: 50%;
    flex: none;
  }
  .card--front .wordmark {
    position: absolute;
    top: 70px;
    right: 44px;
    color: var(--brand);
    font-size: 26px;
  }
  .card--front .wordmark__dot { width: 30px; height: 30px; background: var(--brand); }

  .person {
    position: absolute;
    left: 44px;
    top: 176px;
  }
  .person__name { font-size: 34px; font-weight: 400; line-height: 1.1; }
  .person__title { font-size: 19px; margin-top: 8px; }

  .divider {
    position: absolute;
    left: 44px;
    right: 44px;
    top: 262px;
    height: 2px;
    background: var(--brand);
  }

  .address {
    position: absolute;
    left: 44px;
    top: 290px;
    font-size: 18px;
    line-height: 1.45;
    font-style: normal;
  }

  .contacts {
    position: absolute;
    right: 44px;
    top: 284px;
    list-style: none;
    font-size: 14px;
    line-height: 1;
  }
  .contacts li { display: flex; align-items: center; gap: 12px; margin-bottom: 10px; }
  .contacts svg { width: 13px; height: 13px; fill: var(--brand); flex: none; }
  .contacts .contacts__web { font-weight: 700; }

  .band {
    position: absolute;
    left: 0; right: 0; bottom: 0;
    height: 22px;
    background: var(--brand);
  }

  .card--back .wordmark {
    position: absolute;
    left: 0; right: 0; top: 0; bottom: 0;
    justify-content: center;
    color: var(--paper);
    font-size: 44px;
    gap: 16px;
  }
  .card--back .wordmark__dot { width: 46px; height: 46px; background: var(--paper); }
</style>
</head>
<body>
  <section class="card card--front" aria-label="Business card front">
    <div class="wordmark"><span>Valtrion Tools</span><span class="wordmark__dot"></span></div>

    <div class="person">
      <h1 class="person__name">Daniel Okafor</h1>
      <p class="person__title">Operations Director</p>
    </div>

    <div class="divider"></div>

    <address class="address">
      27 Kallang Way #03-12,<br>
      Meridian Trade Centre,<br>
      Singapore 349281
    </address>

    <ul class="contacts">
      <li>
        <svg viewBox="0 0 16 16" aria-hidden="true"><path d="M4 0h8a1 1 0 0 1 1 1v14a1 1 0 0 1-1 1H4a1 1 0 0 1-1-1V1a1 1 0 0 1 1-1zm1 2v9h6V2zm3 10.5a1 1 0 1 0 0 2 1 1 0 0 0 0-2z"/></svg>
        <span>65-61234567</span>
      </li>
      <li>
        <svg viewBox="0 0 16 16" aria-hidden="true"><path d="M0 3h16v10H0zm1.5 1.2V12h13V4.2L8 9z"/><path d="M1 3.5 8 8.5l7-5" fill="none" stroke="#fff" stroke-width="1"/></svg>
        <span>hello@valtrion.com.sg</span>
      </li>
      <li>
        <svg viewBox="0 0 16 16" aria-hidden="true"><circle cx="8" cy="8" r="8"/><path d="M8 1v14M1 8h14M3 4h10M3 12h10" stroke="#fff" stroke-width="1" fill="none"/></svg>
        <span class="contacts__web">www.valtrion.com.sg</span>
      </li>
    </ul>

    <div class="band"></div>
  </section>

  <section class="card card--back" aria-label="Business card back">
    <div class="wordmark"><span>Valtrion Tools</span><span class="wordmark__dot"></span></div>
  </section>
</body>
</html>
```